Website for a Steadwell, an HVAC company.

We are a company that provides residential and commercial service. We don’t need any widgets other than a call to action where customers can message us. Though we have very few google reviews, they are all great and would like to see those populated. Simple and modern is the style. I included our logo and a pic of our vans.

Target Market(s)

Residential customers

Coding

Coded - Design and coding required

Number of Pages Required

1 page

Font styles to use
Sans Serif

Colors
0054AA
0677BA
7BADD7
CADEEF
E8F1F8
EE7325
F08F49
F5BC92
FAE3D3
FDF4ED

```html
<!DOCTYPE html>
<html lang="en">
<head>
<meta charset="UTF-8">
<title>Steadwell Heating and Air</title>
<link href="https://fonts.googleapis.com/css2?family=Poppins:ital,wght@0,400;0,500;0,600;0,700;1,400&display=swap" rel="stylesheet">
<style>
:root{
  --blue:#3A7BD5;
  --blue-deep:#0054AA;
  --blue-mid:#0677BA;
  --cyan:#2EC5DF;
  --orange:#EE7325;
  --orange-hot:#EE5A1E;
  --gold:#F2AE3C;
  --peach:#FAE3D3;
  --ice:#E8F1F8;
  --text:#2B2B2B;
  --muted:#555;
  --white:#fff;
}
*{box-sizing:border-box;margin:0;padding:0}
html,body{width:1200px;height:4781px;overflow:hidden;background:var(--white)}
body{font-family:'Poppins',sans-serif;color:var(--text)}
.page{position:relative;width:1200px;height:4781px;overflow:hidden}
.abs{position:absolute}
.brand{display:flex;align-items:center;gap:10px;font-weight:700;color:var(--blue);letter-spacing:3px}
.brand-dot{width:34px;height:34px;border-radius:50%;background:var(--orange)}
.pill{display:inline-flex;align-items:center;justify-content:center;border-radius:40px;color:var(--white);font-weight:600;text-transform:uppercase}
.pill-warm{background:linear-gradient(90deg,var(--gold),var(--orange))}
.pill-cool{background:linear-gradient(90deg,var(--blue),var(--cyan))}
.arrow-ring{width:36px;height:36px;border:2px solid var(--white);border-radius:50%;display:flex;align-items:center;justify-content:center;margin-left:16px}
.eyebrow{color:var(--orange);font-weight:500}
.title{color:var(--blue);font-weight:700}
.center{text-align:center;left:0;width:1200px}

/* header */
.header{top:0;left:0;width:1200px;height:139px;background:var(--white)}
.header .brand{position:absolute;left:69px;top:48px;font-size:22px}
.nav{position:absolute;top:57px;font-size:13px;color:var(--text)}
.nav.active{color:var(--orange)}
.btn-book{position:absolute;left:914px;top:41px;width:219px;height:48px;font-size:15px;text-transform:none}

/* hero */
.hero{top:139px;left:0;width:1200px;height:770px;background:linear-gradient(180deg,#F7F9FC,#EEF3F8)}
.hero-photo{position:absolute;right:0;top:0;width:680px;height:770px;background:linear-gradient(90deg,rgba(238,243,248,0) 0%,#DDE5EE 35%,#C9D3DE 70%,#B9C4D1 100%)}
.hero .eyebrow{position:absolute;left:70px;top:115px;font-size:29px;color:var(--gold);font-weight:600}
.hero h1{position:absolute;left:70px;top:155px;font-size:76px;line-height:1;color:var(--blue);font-weight:700;letter-spacing:1px}
.hero h2{position:absolute;left:70px;top:240px;font-size:41px;color:var(--blue);font-weight:600}
.hero p{position:absolute;left:70px;top:305px;width:496px;font-size:17px;line-height:33px;font-weight:500;text-align:justify;color:#222}
.hero .pill{position:absolute;left:70px;top:443px;width:186px;height:52px;font-size:14px}
.hero .arrow-ring{width:32px;height:32px;margin-left:14px}
.hero-waves{position:absolute;left:0;top:550px}
.scroll-cue{position:absolute;left:582px;top:635px;width:36px;height:54px;border:2px solid var(--orange);border-radius:20px;background:var(--white);display:flex;align-items:center;justify-content:center}

/* services */
.svc-eyebrow{top:922px;font-size:25px}
.svc-title{top:955px;font-size:50px}
.svc-intro{top:1038px;left:111px;width:978px;font-size:15px;line-height:27px;text-align:center;color:var(--muted)}
.card{top:1157px;height:520px;background:var(--white);box-shadow:0 4px 14px rgba(0,0,0,.1)}
.card-photo{position:absolute;left:7px;top:8px;right:7px;height:271px}
.card h3{position:absolute;top:308px;width:100%;text-align:center;color:var(--blue);font-size:22px;font-weight:600}
.card p{position:absolute;top:346px;left:38px;right:38px;font-size:15px;line-height:26px;text-align:center;color:var(--muted)}
.card .pill{position:absolute;top:442px;left:50%;transform:translateX(-50%);width:132px;height:40px;font-size:12px}
.view-more{left:506px;width:186px;height:52px;font-size:15px}
.view-more .arrow-ring{width:34px;height:34px}

/* stats */
.stats{top:1836px;left:0}
.stat{position:absolute;color:var(--white)}
.stat b{display:block;font-size:62px;font-weight:500;line-height:1}
.stat i{display:block;width:102px;height:3px;background:var(--white);margin:18px 0 22px}
.stat span{font-size:21px;font-weight:400;letter-spacing:.5px}

/* about */
.about-ring{left:69px;top:2347px;width:500px;height:500px;border:2px solid var(--orange);border-radius:50%}
.about-photo{position:absolute;left:30px;top:30px;width:436px;height:436px;border-radius:50%;background:radial-gradient(circle at 50% 45%,#3C4858,#1A2230 60%,#5E7FA5)}
.about .eyebrow{left:634px;top:2401px;font-size:25px}
.about .title{left:634px;top:2435px;font-size:50px}
.about p{left:634px;top:2520px;width:501px;font-size:15px;line-height:27px;text-align:justify;color:var(--muted)}
.about .pill{left:634px;top:2764px;width:217px;height:65px;font-size:19px;text-transform:uppercase}

/* install band */
.install{top:2912px;left:0}
.install-text{color:var(--white)}
.install .kicker{left:93px;top:3120px;font-size:30px;font-weight:600}
.install h2{left:85px;top:3170px;font-size:62px;line-height:78px;font-weight:700}
.install .pill{left:93px;top:3419px;width:293px;height:86px;font-size:25px;font-weight:700}
.install .arrow-ring{width:56px;height:56px;margin-left:22px}
.van-photo{left:566px;top:3042px;width:634px;height:594px;border-radius:120px 0 0 60px;background:linear-gradient(160deg,#5A6B85 0%,#1B1F2A 45%,#12151C 100%)}

/* testimonials */
.tst-eyebrow{top:3718px;font-size:25px}
.tst-title{top:3750px;font-size:50px}
.quote{top:3845px;height:149px;background:var(--white);box-shadow:0 3px 12px rgba(0,0,0,.1);padding:24px 30px 0}
.quote p{font-size:14px;line-height:25px;font-style:italic;color:var(--muted);text-align:center}
.person{top:4023px;display:flex;align-items:center;gap:14px}
.avatar{width:58px;height:58px;border-radius:50%;background:linear-gradient(135deg,#C9CED6,#8C939E)}
.person h4{font-size:17px;color:var(--blue);font-weight:500;line-height:1.2}
.person small{display:block;font-size:11px;color:var(--text)}
.stars{display:flex;gap:2px;margin-top:3px}

/* footer */
.footer-bg{top:4300px;left:0;width:1200px;height:481px;background:#F4F8FC}
.footer-waves{left:0;top:4205px}
.footer-brand{left:0;width:1200px;top:4430px;display:flex;justify-content:center}
.footer-brand .brand{font-size:26px;letter-spacing:5px}
.contact{top:4560px;display:flex;align-items:center;gap:14px;font-size:13px;line-height:19px}
.contact-icon{width:32px;height:32px;border-radius:6px;background:var(--orange);display:flex;align-items:center;justify-content:center}
.rule{left:70px;width:1063px;height:1px;background:var(--orange)}
.fnav{top:4667px;font-size:13px}
.copy{left:70px;top:4739px;font-size:10px}
.social{top:4736px;width:26px;height:26px;border-radius:4px;background:var(--blue)}
</style>
</head>
<body>
<div class="page">

  <!-- header -->
  <header class="abs header">
    <div class="brand"><span class="brand-dot"></span>STEADWELL</div>
    <span class="nav active" style="left:293px">HOME</span>
    <span class="nav" style="left:382px">ABOUT US</span>
    <span class="nav" style="left:497px">OUR SERVICES</span>
    <span class="nav" style="left:642px">TESTIMONIALS</span>
    <span class="nav" style="left:785px">CONTACT US</span>
    <a class="pill pill-warm btn-book">Book An Appointment</a>
  </header>

  <!-- hero -->
  <section class="abs hero">
    <div class="hero-photo" role="img" aria-label="Close-up of a hand adjusting the vane of a wall-mounted air conditioner"></div>
    <div class="eyebrow">WELCOME TO</div>
    <h1>STEADWELL</h1>
    <h2>HEATING AND AIR</h2>
    <p>Lorem ipsum dolor sit amet, consectetur adipiscing elit, sed do eiusmod tempor incididunt ut labore et dolore magna aliqua. Quis ipsum suspendisse ultrices gravida.</p>
    <a class="pill pill-warm">Learn More<span class="arrow-ring"><svg width="14" height="14" viewBox="0 0 14 14"><path d="M3 11L11 3M5 3h6v6" stroke="#fff" stroke-width="2" fill="none"/></svg></span></a>
    <svg class="hero-waves" width="1200" height="220" viewBox="0 0 1200 220">
      <path d="M0,170 C200,40 400,0 600,40 C750,70 780,120 800,130 L800,110 C620,20 380,20 0,140 Z" fill="#F5BC92"/>
      <path d="M0,200 C200,60 420,20 620,80 C820,140 980,170 1200,40 L1200,220 L0,220 Z" fill="#EFA43A"/>
      <path d="M0,220 C210,90 420,50 620,100 C820,150 1000,190 1200,70 L1200,220 Z" fill="#fff"/>
      <path d="M760,150 C900,190 1060,170 1200,60 L1200,90 C1060,190 900,205 760,160 Z" fill="#3A7BD5"/>
      <path d="M800,175 C950,205 1080,180 1200,95 L1200,110 C1080,195 950,215 800,182 Z" fill="#7BADD7"/>
    </svg>
    <div class="scroll-cue"><svg width="14" height="18" viewBox="0 0 14 18"><path d="M7 2v13M2 10l5 5 5-5" stroke="#EE7325" stroke-width="2" fill="none"/></svg></div>
  </section>

  <!-- services -->
  <div class="abs center eyebrow svc-eyebrow">What We Do</div>
  <h2 class="abs center title svc-title">OUR SERVICES</h2>
  <p class="abs svc-intro">Lorem ipsum dolor sit amet, consectetur adipiscing elit, sed do eiusmod tempor incididunt ut labore et dolore magna aliqua. Ut enim ad minim veniam, quis nostrud exercitation ullamco laboris nisi ut aliquip ex ea commodo consequat. Duis aute irure dolor in reprehenderit in voluptate velit esse cillum dolore eu fugiat nulla pariatur. L</p>

  <article class="abs card" style="left:70px;width:340px">
    <div class="card-photo" role="img" aria-label="Two technicians servicing a ceiling duct unit" style="background:linear-gradient(160deg,#D9DEE4,#6E6A68)"></div>
    <h3>SERVICE 1</h3>
    <p>Lorem ipsum dolor sit amet, consec tetur adipiscing elit, sed do eiusmod tempor incididunt</p>
    <a class="pill pill-cool">Read More</a>
  </article>
  <article class="abs card" style="left:430px;width:334px">
    <div class="card-photo" role="img" aria-label="Technician cleaning a wall-mounted split air conditioner" style="background:linear-gradient(160deg,#F1F1F1,#A8A8A8)"></div>
    <h3>SERVICE 2</h3>
    <p>Lorem ipsum dolor sit amet, consec tetur adipiscing elit, sed do eiusmod tempor incididunt</p>
    <a class="pill pill-cool">Read More</a>
  </article>
  <article class="abs card" style="left:792px;width:341px">
    <div class="card-photo" role="img" aria-label="Technician with clipboard inspecting an indoor AC unit" style="background:linear-gradient(160deg,#CFCFCF,#6C8FB8)"></div>
    <h3>SERVICE 3</h3>
    <p>Lorem ipsum dolor sit amet, consec tetur adipiscing elit, sed do eiusmod tempor incididunt</p>
    <a class="pill pill-cool">Read More</a>
  </article>

  <a class="abs pill pill-warm view-more" style="top:1751px">View More<span class="arrow-ring"><svg width="14" height="14" viewBox="0 0 14 14"><path d="M3 11L11 3M5 3h6v6" stroke="#fff" stroke-width="2" fill="none"/></svg></span></a>

  <!-- stats -->
  <svg class="abs stats" width="1200" height="490" viewBox="0 0 1200 490">
    <defs><linearGradient id="statsGrad" x1="0" x2="1"><stop offset="0" stop-color="#4A7EE0"/><stop offset="1" stop-color="#2EC5DF"/></linearGradient></defs>
    <path d="M0,160 C180,20 420,30 620,90 C820,150 1000,120 1200,40 L1200,440 C1000,490 800,440 600,390 C400,340 200,380 0,460 Z" fill="url(#statsGrad)"/>
  </svg>
  <div class="stat" style="left:108px;top:2000px"><b>10+</b><i></i><span>YEARS OF EXPERIENCE</span></div>
  <div class="stat" style="left:404px;top:2000px"><b>20+</b><i></i><span>PROFESSIONAL TEAM</span></div>
  <div class="stat" style="left:696px;top:2000px"><b>10K</b><i></i><span>HAPPY CUSTOMERS</span></div>
  <div class="stat" style="left:979px;top:2000px"><b>10</b><i></i><span>BRANCHES</span></div>

  <!-- about -->
  <section class="about">
    <div class="abs about-ring"><div class="about-photo" role="img" aria-label="Company service van parked outside an office building"></div></div>
    <div class="abs eyebrow">Who We Are</div>
    <h2 class="abs title">ABOUT US</h2>
    <p class="abs">Lorem ipsum dolor sit amet, consectetur adipiscing elit, sed do eiusmod tempor incididunt ut labore et dolore magna aliqua. Ut enim ad minim veniam, quis nostrud exercitation ullamco laboris nisi ut aliquip ex ea commodo consequat. Duis aute irure dolor in reprehenderit in voluptate velit esse cillum dolore eu fugiat nulla pariatur. Lorem ipsum dolor sit amet, consectetur adipiscing elit, sed do eiusmod tempor incididunt ut labore et dolore magna aliqua. Ut enim ad minim veniam, quis nostrud exercitation ullamco laboris nisi ut aliquip ex ea commodo .</p>
    <a class="abs pill pill-cool">Know More</a>
  </section>

  <!-- installation band -->
  <section class="install">
    <svg class="abs" style="left:0;top:2912px" width="1200" height="760" viewBox="0 0 1200 760">
      <defs><linearGradient id="installGrad" x1="0" x2="1"><stop offset="0" stop-color="#EE5A1E"/><stop offset=".6" stop-color="#F08F2E"/><stop offset="1" stop-color="#F2B844"/></linearGradient></defs>
      <path d="M0,110 C220,10 420,140 680,90 C880,50 1040,0 1200,20 L1200,640 C1000,740 800,690 580,700 C380,712 180,680 0,560 Z" fill="url(#installGrad)"/>
    </svg>
    <div class="abs van-photo" role="img" aria-label="Black company service van with ladder rack, side view"></div>
    <div class="abs install-text kicker">AIR CONDITIONING SERVICES</div>
    <h2 class="abs install-text">BEST AIR<br>CONDITIONING<br>INSTALLATION</h2>
    <a class="abs pill pill-cool">Contact Us<span class="arrow-ring"><svg width="22" height="22" viewBox="0 0 14 14"><path d="M3 11L11 3M5 3h6v6" stroke="#fff" stroke-width="2" fill="none"/></svg></span></a>
  </section>

  <!-- testimonials -->
  <div class="abs center eyebrow tst-eyebrow">Reviews</div>
  <h2 class="abs center title tst-title">OUR TESTIMONIALS</h2>

  <div class="abs quote" style="left:69px;width:341px"><p>Lorem ipsum dolor sit amet, conse ctetuer adipiscing elit. Aenean comodo ligula eget dolor. Aenean massa. Cum sociis natoque pen atibus et magnis</p></div>
  <div class="abs quote" style="left:430px;width:340px"><p>Lorem ipsum dolor sit amet, conse ctetuer adipiscing elit. Aenean comodo ligula eget dolor. Aenean massa. Cum sociis natoque pen atibus et magnis</p></div>
  <div class="abs quote" style="left:792px;width:341px"><p>Lorem ipsum dolor sit amet, conse ctetuer adipiscing elit. Aenean comodo ligula eget dolor. Aenean massa. Cum sociis natoque pen atibus et magnis</p></div>

  <div class="abs person" style="left:134px"><div class="avatar" role="img" aria-label="Reviewer portrait"></div><div><h4>Marcus Reed</h4><small>Managing Director</small><div class="stars"><svg width="70" height="12" viewBox="0 0 70 12"><g fill="#F2AE3C"><path id="st" d="M6 0l1.8 3.8 4.2.5-3.1 2.9.8 4.1L6 9.3 2.3 11.3l.8-4.1L0 4.3l4.2-.5z"/><use href="#st" x="14"/><use href="#st" x="28"/><use href="#st" x="42"/><use href="#st" x="56"/></g></svg></div></div></div>
  <div class="abs person" style="left:495px"><div class="avatar" role="img" aria-label="Reviewer portrait"></div><div><h4>Dana Holt</h4><small>Managing Director</small><div class="stars"><svg width="70" height="12" viewBox="0 0 70 12"><g fill="#F2AE3C"><use href="#st"/><use href="#st" x="14"/><use href="#st" x="28"/><use href="#st" x="42"/><use href="#st" x="56"/></g></svg></div></div></div>
  <div class="abs person" style="left:855px"><div class="avatar" role="img" aria-label="Reviewer portrait"></div><div><h4>Priya Nolan</h4><small>Managing Director</small><div class="stars"><svg width="70" height="12" viewBox="0 0 70 12"><g fill="#F2AE3C"><use href="#st"/><use href="#st" x="14"/><use href="#st" x="28"/><use href="#st" x="42"/><use href="#st" x="56"/></g></svg></div></div></div>

  <a class="abs pill pill-warm view-more" style="top:4149px">View More<span class="arrow-ring"><svg width="14" height="14" viewBox="0 0 14 14"><path d="M3 11L11 3M5 3h6v6" stroke="#fff" stroke-width="2" fill="none"/></svg></span></a>

  <!-- footer -->
  <div class="abs footer-bg"></div>
  <svg class="abs footer-waves" width="1200" height="190" viewBox="0 0 1200 190">
    <path d="M0,110 C150,20 350,30 520,110 C400,70 200,70 0,160 Z" fill="#7BADD7"/>
    <path d="M0,150 C160,60 360,60 560,130 C380,100 190,110 0,190 Z" fill="#3A7BD5"/>
    <path d="M0,190 C190,110 380,100 560,130 C760,165 980,150 1200,60 L1200,190 Z" fill="#F4F8FC"/>
    <path d="M700,170 C900,170 1060,110 1200,0 L1200,40 C1060,140 900,180 700,172 Z" fill="#F5BC92"/>
    <path d="M760,175 C940,170 1080,120 1200,40 L1200,80 C1080,150 940,180 760,176 Z" fill="#EE7325"/>
  </svg>
  <div class="abs footer-brand"><div class="brand"><span class="brand-dot" style="width:40px;height:40px"></span>STEADWELL</div></div>

  <div class="abs contact" style="left:256px"><span class="contact-icon"><svg width="16" height="16" viewBox="0 0 16 16"><path d="M3 1l3 3-2 2c1 2 3 4 5 5l2-2 3 3-2 3C7 15 1 9 1 3z" fill="#fff"/></svg></span><div>CALL US<br>555-014-2290</div></div>
  <div class="abs contact" style="left:479px"><span class="contact-icon"><svg width="16" height="12" viewBox="0 0 16 12"><rect x="1" y="1" width="14" height="10" fill="none" stroke="#fff" stroke-width="1.6"/><path d="M1 1l7 6 7-6" fill="none" stroke="#fff" stroke-width="1.6"/></svg></span><div>EMAIL US<br>hello@steadwellair.com</div></div>
  <div class="abs contact" style="left:720px"><span class="contact-icon"><svg width="14" height="18" viewBox="0 0 14 18"><path d="M7 0a7 7 0 0 1 7 7c0 5-7 11-7 11S0 12 0 7a7 7 0 0 1 7-7z" fill="#fff"/><circle cx="7" cy="7" r="2.5" fill="#EE7325"/></svg></span><div>Address line Dummy Here<br>Address line Here</div></div>

  <div class="abs rule" style="top:4637px"></div>
  <span class="abs fnav" style="left:309px">HOME</span>
  <span class="abs fnav" style="left:398px">ABOUT US</span>
  <span class="abs fnav" style="left:513px">OUR SERVICES</span>
  <span class="abs fnav" style="left:658px">TESTIMONIALS</span>
  <span class="abs fnav" style="left:800px">CONTACT US</span>
  <div class="abs rule" style="top:4711px"></div>
  <div class="abs copy">Copyright © 2025 All Rights Reserved By Company name</div>
  <span class="abs social" style="left:1014px"></span>
  <span class="abs social" style="left:1045px"></span>
  <span class="abs social" style="left:1076px"></span>
  <span class="abs social" style="left:1107px"></span>

</div>
</body>
</html>
```